Creation of a book cover
Size : 14 x 20,5 cm (+ 5 mm bleed area at the top, bottom and right areas)
The Title is a French sentence which means “The fly washing its hands in a glass of water”. It’s a surrealistic title which has no link to the story.
AUTHOR : Mathieu Vaudrelle
TITLE : "Le hibou qui comptait les étoiles au fond d’un puits sec »
PUBLISHER (AT THE BOTTOM OF THE PAGE) : Editions Portemine
I send a PDF file with the kind of cover we have imagine, but you can propose something different. The glass and the fly can of course be used.

```html
<!DOCTYPE html>
<html lang="fr">
<head>
<meta charset="utf-8">
<title>Le hibou qui comptait les étoiles au fond d’un puits sec — Mathieu Vaudrelle</title>
<link rel="stylesheet" href="https://fonts.googleapis.com/css2?family=Bebas+Neue&family=Roboto+Condensed:wght@500&family=Rubik+Wet+Paint&family=Cabin:wght@400&display=swap">
<style>
  :root {
    --backdrop: #ebe4d8;
    --paper: #ffffff;
    --grid-line: #e3e5e8;
    --ink: #111111;
    --blood-red: #7d0a0a;
    --glass-light: #dfe6e8;
    --glass-dark: #8c9da2;
  }
  * { margin: 0; padding: 0; box-sizing: border-box; }
  html, body {
    width: 960px;
    height: 1200px;
    overflow: hidden;
    background: var(--backdrop);
  }
  .book-cover {
    position: absolute;
    left: 105px;
    top: 51px;
    width: 750px;
    height: 1098px;
    background-color: var(--paper);
    background-image:
      linear-gradient(var(--grid-line) 2px, transparent 2px),
      linear-gradient(90deg, var(--grid-line) 2px, transparent 2px);
    background-size: 46px 46px;
    background-position: 12px 10px;
    box-shadow: 0 10px 30px rgba(60, 50, 35, 0.18);
    text-align: center;
  }
  .author {
    position: absolute;
    top: 168px;
    left: 0;
    right: 0;
    font-family: "Roboto Condensed", sans-serif;
    font-weight: 500;
    font-size: 30px;
    letter-spacing: 3px;
    color: var(--ink);
  }
  .title {
    position: absolute;
    top: 350px;
    left: 0;
    right: 0;
  }
  .title-lead {
    display: block;
    font-family: "Rubik Wet Paint", cursive;
    font-size: 96px;
    line-height: 1;
    color: var(--blood-red);
    text-transform: uppercase;
  }
  .title-rest {
    display: block;
    margin-top: 10px;
    font-family: "Bebas Neue", sans-serif;
    font-size: 62px;
    line-height: 1.02;
    color: var(--ink);
    text-transform: uppercase;
  }
  .cover-illustration {
    position: absolute;
    left: 50%;
    top: 640px;
    width: 220px;
    height: 270px;
    margin-left: -110px;
    border-radius: 10px 10px 36px 36px;
    background: linear-gradient(180deg, var(--glass-light) 0%, var(--glass-dark) 100%);
  }
  .publisher {
    position: absolute;
    bottom: 96px;
    left: 0;
    right: 0;
    font-family: "Cabin", sans-serif;
    font-size: 26px;
    color: var(--ink);
  }
</style>
</head>
<body>
  <main class="book-cover">
    <p class="author">Mathieu Vaudrelle</p>
    <h1 class="title">
      <span class="title-lead">Le hibou</span>
      <span class="title-rest">qui comptait les étoiles<br>au fond d’un puits sec</span>
    </h1>
    <div class="cover-illustration" role="img" aria-label="Illustration : un verre d’eau avec un insecte posé sur le bord"></div>
    <p class="publisher">Éditions Portemine</p>
  </main>
</body>
</html>
```